Business Card Design

I need a card design for Melbourne based business in Australia, called T W Concrete Services. We Concrete and excavate. Concreteing is main part of business.Commercial ,Residential and industrial.We want to be known as T W C (services) as form of abbreviation.We would like to highlight the initials with contact phone. A clean straight edge design. We have no color preference and would prefer a design that can easily be used on all parts of our business including clothing,vechiles and stationary

Industry/Entity Type

Business

Contact Information for Business Card

Colin 0412 905 268
Barry 0421 574 360
twcsercices@quokkanet.com

```html
<!DOCTYPE html>
<html lang="en">
<head>
<meta charset="utf-8">
<title>T W C Concrete &amp; Excavation — Business Card</title>
<link href="https://fonts.googleapis.com/css2?family=Didact+Gothic&family=Comfortaa:wght@300&display=swap" rel="stylesheet">
<style>
  :root {
    --page-bg: #e6e4e0;
    --charcoal-dark: #262626;
    --charcoal-mid: #3c3c3c;
    --charcoal-light: #555555;
    --paper: #ffffff;
    --paper-shade: #ececec;
    --label-bg: #d9d9d9;
    --label-text: #2e2e2e;
    --ink-light: #f4f4f4;
    --machine-yellow: #f2c318;
    --machine-grey: #6b6f73;
  }
  * { box-sizing: border-box; margin: 0; padding: 0; }
  html, body {
    width: 1200px; height: 900px; overflow: hidden;
    background: var(--page-bg);
  }
  .sheet {
    position: relative; width: 1200px; height: 900px;
    display: flex; flex-direction: column; align-items: center; justify-content: center; gap: 48px;
  }
  .card {
    position: relative; width: 580px; height: 350px; overflow: hidden;
    box-shadow: 0 6px 18px rgba(0,0,0,0.18);
  }

  /* Front */
  .card-front {
    background: linear-gradient(135deg, var(--charcoal-light) 0%, var(--charcoal-mid) 45%, var(--charcoal-dark) 100%);
    color: var(--ink-light);
    font-family: "Didact Gothic", sans-serif;
  }
  .wordmark {
    position: absolute; left: 40px; top: 28px;
    font-family: "Comfortaa", sans-serif; font-weight: 300;
    font-size: 100px; line-height: 1; letter-spacing: 2px;
    color: var(--ink-light);
  }
  .divider-line {
    position: absolute; left: 0; top: 0; width: 580px; height: 350px;
    pointer-events: none;
  }
  .tagline {
    position: absolute; left: 44px; top: 170px;
    font-size: 24px; line-height: 1.2; letter-spacing: 0.5px;
  }
  .contacts { position: absolute; left: 44px; top: 212px; }
  .contact-row { display: flex; align-items: center; gap: 14px; margin-bottom: 8px; }
  .contact-name {
    display: inline-block; width: 112px; padding: 2px 10px;
    background: var(--label-bg); color: var(--label-text);
    font-size: 23px; line-height: 1.2; letter-spacing: 1px; text-transform: uppercase;
  }
  .contact-phone { font-size: 26px; line-height: 1.2; letter-spacing: 1px; }
  .email {
    position: absolute; left: 44px; top: 304px;
    font-size: 22px; line-height: 1.2; letter-spacing: 0.3px;
  }

  /* Back */
  .card-back { background: linear-gradient(180deg, var(--paper) 0%, var(--paper-shade) 100%); }
  .back-band { position: absolute; left: 0; top: 0; width: 200px; height: 350px; }
  .machine-photo {
    position: absolute; left: 200px; top: 30px; width: 350px; height: 290px;
    background: linear-gradient(160deg, var(--machine-grey) 0%, var(--machine-yellow) 55%, var(--charcoal-dark) 100%);
    border-radius: 6px; opacity: 0.9;
  }
</style>
</head>
<body>
<main class="sheet">
  <section class="card card-front" aria-label="Card front">
    <div class="wordmark">T W C</div>
    <svg class="divider-line" viewBox="0 0 580 350" aria-hidden="true">
      <line x1="150" y1="160" x2="420" y2="126" stroke="#f4f4f4" stroke-width="2"/>
    </svg>
    <div class="tagline">Concrete &amp; Excavation</div>
    <div class="contacts">
      <div class="contact-row"><span class="contact-name">Colin</span><span class="contact-phone">0412 905 268</span></div>
      <div class="contact-row"><span class="contact-name">Barry</span><span class="contact-phone">0421 574 360</span></div>
    </div>
    <div class="email">twcsercices@quokkanet.com</div>
  </section>

  <section class="card card-back" aria-label="Card back">
    <svg class="back-band" viewBox="0 0 200 350" aria-hidden="true">
      <defs>
        <linearGradient id="bandShade" x1="0" y1="0" x2="1" y2="1">
          <stop offset="0" stop-color="#555555"/>
          <stop offset="1" stop-color="#262626"/>
        </linearGradient>
      </defs>
      <polygon points="0,0 70,0 140,175 70,350 0,350" fill="url(#bandShade)"/>
      <polyline points="82,0 152,175 82,350" fill="none" stroke="#9a9a9a" stroke-width="3"/>
    </svg>
    <div class="machine-photo" role="img" aria-label="Photograph of a yellow and grey compact excavator with its arm raised"></div>
  </section>
</main>
</body>
</html>
```